CREATIVE DESIGNERS NEEDED & Enhance Your Business Card Portfolio

Artistic, unique, professional real estate card needed - see attached documents "B-cards.pdf" for all details and examples.True Designers will see other projects of ours come online here. We like long-term relationships for creative designers. This business card will be used in two U.S. states and is central to our business and other future marketing.

Target Market(s)

Buyers and Sellers of real estate

Industry/Entity Type

Real Estate Agent

Contact Information for Business Card

See attached detailed brief

Other font styles liked:
• ADAM.CG PRO & NewsGoth BT

Requirements
Must have
• 2-sided, creative (non-traditional layout/design). Incorporate a cut-out (for texture, and make it fun! No boring templates for this card -
Nice to have
• See attached detailed brief
Should not have

```html
<!DOCTYPE html>
<html lang="en">
<head>
<meta charset="UTF-8">
<title>Harlow Reed Group – Business Card</title>
<link rel="stylesheet" href="https://fonts.googleapis.com/css2?family=Montserrat:wght@400;500;600;700&display=swap">
<style>
  :root {
    --brand-red: #c02126;
    --brand-navy: #27303f;
    --ink-grey: #4a4a4a;
    --paper: #ffffff;
    --backdrop: #e9e7e4;
    --portrait-top: #3a2c24;
    --portrait-mid: #cfa28b;
    --portrait-low: #1f2230;
  }
  * { box-sizing: border-box; margin: 0; padding: 0; }
  html, body { width: 1200px; height: 930px; overflow: hidden; }
  body {
    background: var(--backdrop);
    font-family: "Montserrat", sans-serif;
    position: relative;
  }

  /* Shell carries the shadow so the die-cut stays visible */
  .card-shell {
    position: absolute;
    width: 540px;
    height: 310px;
    filter: drop-shadow(0 6px 12px rgba(0,0,0,0.18));
  }
  .card-shell--front { left: 90px; top: 110px; }
  .card-shell--back { left: 570px; top: 510px; }

  .card {
    position: relative;
    width: 100%;
    height: 100%;
    border-radius: 16px;
    overflow: hidden;
  }
  /* Die-cut notch punched through the left edge */
  .card--diecut {
    -webkit-mask: radial-gradient(circle at 0 50%, transparent 26px, #000 27px);
            mask: radial-gradient(circle at 0 50%, transparent 26px, #000 27px);
  }
  .card--diecut-top {
    -webkit-mask: radial-gradient(circle at 100% 0, transparent 26px, #000 27px);
            mask: radial-gradient(circle at 100% 0, transparent 26px, #000 27px);
  }

  /* Front side */
  .card--front {
    background: var(--brand-red);
    display: flex; align-items: center; justify-content: center;
  }
  .wordmark {
    display: flex; align-items: center; gap: 14px;
    color: var(--paper);
  }
  .wordmark__square {
    width: 58px; height: 58px;
    background: var(--paper);
  }
  .wordmark__name {
    font-weight: 600;
    font-size: 30px;
    line-height: 1.05;
    letter-spacing: 1px;
    text-transform: uppercase;
  }
  .wordmark__name span { display: block; }
  .wordmark__name .small { font-size: 15px; font-weight: 500; letter-spacing: 5px; margin-top: 4px; }

  /* Back side */
  .card--back { background: var(--paper); }
  .portrait {
    position: absolute;
    left: 44px; top: 66px;
    width: 216px; height: 236px;
    border-radius: 108px 108px 0 0;
    background: linear-gradient(180deg, var(--portrait-top) 0%, var(--portrait-mid) 34%, var(--portrait-mid) 64%, var(--portrait-low) 100%);
  }
  .back-mark {
    position: absolute; right: 34px; top: 28px;
    display: flex; align-items: center; gap: 10px;
    color: var(--brand-navy);
  }
  .back-mark__square { width: 40px; height: 40px; background: var(--brand-navy); }
  .back-mark__name {
    font-weight: 600; font-size: 19px; line-height: 1.05;
    text-transform: uppercase; letter-spacing: 1px;
  }
  .back-mark__name span { display: block; }
  .back-mark__name .small { font-size: 10px; font-weight: 500; letter-spacing: 3px; margin-top: 3px; color: var(--brand-red); }

  .name-flag {
    position: absolute; right: 0; top: 110px;
    width: 12px; height: 30px; background: var(--brand-red);
  }
  .agent {
    position: absolute; right: 34px; top: 108px;
    text-align: right;
  }
  .agent__name {
    color: var(--brand-red);
    font-weight: 600; font-size: 22px;
    text-transform: uppercase; letter-spacing: 0.5px;
    line-height: 1.1;
  }
  .agent__title { color: var(--ink-grey); font-size: 11px; margin-top: 2px; }

  .contacts {
    position: absolute; right: 28px; top: 166px;
    list-style: none; text-align: right;
    color: var(--ink-grey); font-size: 12px; line-height: 1.45;
  }
  .contacts li { display: flex; justify-content: flex-end; align-items: center; gap: 6px; }
  .contacts svg { width: 10px; height: 10px; fill: var(--brand-red); }

  .band { position: absolute; left: 0; bottom: 0; width: 540px; height: 72px; }
  .address {
    position: absolute; right: 26px; bottom: 14px;
    color: var(--paper); text-align: right;
    font-size: 12px; line-height: 1.45;
  }
</style>
</head>
<body>
  <div class="card-shell card-shell--front">
    <section class="card card--front card--diecut">
      <div class="wordmark">
        <div class="wordmark__square"></div>
        <div class="wordmark__name">
          <span>Harlow Reed</span>
          <span>Group</span>
          <span class="small">Real Estate</span>
        </div>
      </div>
    </section>
  </div>

  <div class="card-shell card-shell--back">
    <section class="card card--back card--diecut">
      <div class="portrait" role="img" aria-label="Headshot photograph of the agent in a dark suit"></div>

      <div class="back-mark">
        <div class="back-mark__square"></div>
        <div class="back-mark__name">
          <span>Harlow Reed</span>
          <span>Group</span>
          <span class="small">Real Estate</span>
        </div>
      </div>

      <div class="name-flag"></div>
      <div class="agent">
        <div class="agent__name">Daniel Carter</div>
        <div class="agent__title">Director</div>
      </div>

      <ul class="contacts">
        <li>555-014-2290
          <svg viewBox="0 0 10 10"><path d="M2 0.5 L3.8 2.6 L2.9 3.6 Q4 6 6.4 7.1 L7.4 6.2 L9.5 8 L8.2 9.5 Q1 8 0.5 1.8 Z"/></svg></li>
        <li>info@harlowreedgroup.com
          <svg viewBox="0 0 10 10"><path d="M0.5 2 H9.5 V8 H0.5 Z M1.2 2.6 L5 5.4 L8.8 2.6 V7.4 H1.2 Z" fill-rule="evenodd"/></svg></li>
        <li>www.harlowreedgroup.com
          <svg viewBox="0 0 10 10"><circle cx="5" cy="5" r="4.5"/></svg></li>
      </ul>

      <svg class="band" viewBox="0 0 540 72" preserveAspectRatio="none" aria-hidden="true">
        <path d="M0 62 L300 62 L318 8 L540 8 L540 72 L0 72 Z" fill="var(--brand-red)"/>
      </svg>
      <div class="address">
        88-90 Birch Avenue West<br>
        Lakeford, Ontario K2R 4M6
      </div>
    </section>
  </div>
</body>
</html>
```